Production company require television show pitch document cover design

We're StoneHarbor Pictures — a television production company based in Canberra, Australia — and we're pitching a television show idea at an upcoming conference. The show's called "Frontline Reef Patrols", and it's about an elite Tasmanian whale rescue team who race the clock to save the lives of charismatic megafauna. That's where you come in! We need the pitch document to be eye-catching and draw potential investors in to the story we're trying to tell. Are you up for it?

We need a fully designed A4 cover page.

I've attached the two page pitch document to give you an idea of what the show's about. I've also attached the two logos of the production companies involved, an example of a pitch document ("Restless Tides") and some images of beached whales (for inspiration).

There are a couple of things we specifically need on the cover page but otherwise you're free to get creative!
Updates

Project Deadline Extended
Reason: As it's a public holiday on Monday, we wouldn't have time to properly review designs and provide feedback, so we're extending the deadline by 5 days.

Target Market(s)

International broadcasters.

Industry/Entity Type

It Company

Font styles to use
Sans Serif

Requirements
Must have
• Both logos featured (usually at the bottom of the cover page).
Logline (or tagline) featured: "On watch 24/7, Tasmania’s elite Whale Rescue team race the clock to the save the lives of stranded giants wherever they may be on the island’s rugged coastline."
[Factual series] written in top right hand corner (see example pitch document).

```html
<!DOCTYPE html>
<html lang="en">
<head>
<meta charset="utf-8">
<title>Frontline Reef Patrols – Pitch Cover</title>
<link rel="stylesheet" href="https://fonts.googleapis.com/css2?family=Orbitron:wght@800;900&family=Arimo:wght@400;700&family=Lato:wght@400&display=swap">
<style>
  :root {
    --page-bg: #e7e4df;
    --panel: #313234;
    --accent: #1ba3e8;
    --accent-bright: #36b4f0;
    --white: #ffffff;
    --sea-deep: #1b3f78;
    --sea-mid: #2d5f9e;
    --sea-light: #5b8fc8;
    --sea-foam: #8fb4dc;
  }
  * { margin: 0; padding: 0; box-sizing: border-box; }
  html, body {
    width: 907px; height: 1200px; overflow: hidden;
    background: var(--page-bg);
  }
  .cover {
    position: absolute; left: 72px; top: 62px;
    width: 766px; height: 1078px;
    background: var(--panel);
    overflow: hidden;
  }
  .bracket { position: absolute; background: var(--accent); }
  .bracket--top-bar { left: 0; top: 0; width: 441px; height: 34px; }
  .bracket--left-bar { left: 0; top: 0; width: 34px; height: 238px; }
  .bracket--right-bar { right: 0; bottom: 0; width: 34px; height: 200px; }
  .bracket--bottom-bar { right: 0; bottom: 0; width: 424px; height: 34px; }

  .format-label {
    position: absolute; left: 583px; top: 49px;
    width: 145px; height: 39px;
    border: 1.5px solid var(--white);
    color: var(--white);
    font: 400 20px/36px "Lato", sans-serif;
    text-align: center;
  }

  .hero-frame {
    position: absolute; left: 83px; top: 83px;
    width: 635px; height: 597px;
    border: 6px solid var(--accent);
    border-radius: 300px 300px 300px 0;
    overflow: hidden;
  }
  .hero-photo {
    width: 100%; height: 100%;
    background:
      radial-gradient(ellipse 60% 22% at 58% 62%, rgba(220,230,240,0.45) 0%, rgba(143,180,220,0.2) 50%, rgba(143,180,220,0) 100%),
      linear-gradient(175deg, var(--sea-light) 0%, var(--sea-mid) 40%, var(--sea-mid) 60%, var(--sea-deep) 100%);
  }

  .title {
    position: absolute; left: 36px; top: 704px;
    font-family: "Orbitron", sans-serif; font-weight: 900;
    text-transform: uppercase; line-height: 1;
  }
  .title__top { display: block; color: var(--white); font-size: 62px; letter-spacing: 1px; }
  .title__bottom { display: block; color: var(--accent-bright); font-size: 60px; margin-top: 12px; letter-spacing: 1px; }

  .logline {
    position: absolute; left: 0; top: 858px;
    width: 673px; height: 83px;
    background: var(--accent);
    border-radius: 0 30px 30px 0;
    padding: 7px 0 0 37px;
    color: var(--white);
    font: 700 22px/22px "Arimo", sans-serif;
    font-variant: small-caps;
    letter-spacing: 0.6px;
  }
  .logline__line { display: block; white-space: nowrap; }

  .partners {
    position: absolute; left: 38px; top: 956px;
    display: flex; gap: 14px; align-items: flex-start;
  }
  .partner {
    display: flex; flex-direction: column; align-items: center; gap: 10px;
    width: 150px;
    color: var(--white);
    font: 400 17px/1 "Arimo", sans-serif;
    white-space: nowrap;
  }
  .partner:first-child { width: 120px; }
  .partner__mark {
    width: 60px; height: 60px; border-radius: 50%;
    border: 3px solid var(--white);
  }
</style>
</head>
<body>
  <main class="cover">
    <div class="bracket bracket--top-bar"></div>
    <div class="bracket bracket--left-bar"></div>
    <div class="bracket bracket--right-bar"></div>
    <div class="bracket bracket--bottom-bar"></div>

    <div class="format-label">Factual Series</div>

    <div class="hero-frame">
      <div class="hero-photo" role="img" aria-label="Rescue crew in an inflatable boat freeing a whale entangled in buoys at sea"></div>
    </div>

    <h1 class="title">
      <span class="title__top">Frontline</span>
      <span class="title__bottom">Reef Patrols</span>
    </h1>

    <p class="logline">
      <span class="logline__line">On watch 24/7, Tasmania’s elite Whale Rescue team</span>
      <span class="logline__line">race the clock to the save the lives of stranded giants</span>
      <span class="logline__line">wherever they may be on the island’s rugged coastline</span>
    </p>

    <footer class="partners">
      <div class="partner"><span class="partner__mark"></span>Kestrel Films</div>
      <div class="partner"><span class="partner__mark"></span>StoneHarbor Pictures</div>
    </footer>
  </main>
</body>
</html>
```